Flyer, poster, banner and social media titles designs for Community Renewal Guidlines

The Shared Guidelines for Community Renewal provide a nationally agreed framework to guide recovery policy and practice across Australia. The Principles support recovery practitioners, governments, non-government organisations and communities to deliver effective, community-centred recovery outcomes.
The Principles have recently been refreshed through extensive consultation and we require a contemporary visual identity and design suite that will increase awareness, engagement and practical application of the Principles.
The redesign will cover:
• A4 Brochure (primary publication)
• A3 Poster
• Pull up banner
• Social Media Tiles
The new design should:
• Create a recognisable brand for the Shared Guidelines.
• Appeal to both experienced and emerging recovery practitioners.
• Reflect contemporary disaster recovery practice.
• Feel people-focused rather than government-focused.
• Support future resources such as videos, implementation guides, presentations and workshop materials.
• Remain relevant for several years without requiring a major redesign.
Target Audience
• Disaster recovery practitioners
• Government agencies
• Non-government organisations
• Community recovery workers
• Recovery managers and leaders
• Community stakeholders and volunteers
The visual identity should reflect the six Principles:
• Understanding Context
• Recognising Complexity
• Community-Centred Approaches
• Coordination
• Communication
• Capacity Building
The design should communicate:
• Recovery is centred on people and communities.
• Recovery is collaborative and involves many sectors.
• Recovery is adaptive, inclusive and evidence-informed.
• Recovery supports resilience and long-term wellbeing.
• The Principles provide practical guidance for recovery practice.
We are looking for:
• Modern and professional
• Warm and approachable
• Human-centred
• Inclusive and accessible
• Australian in context
• Visually engaging
• Suitable for print and digital use
We would like to avoid:
• Images of disaster destruction
• Emergency response imagery (fire trucks, flashing lights, etc.)
• Overly corporate or bureaucratic designs
• Designs that focus on deficits rather than recovery and growth
Consider themes such as:
• Connection and collaboration
• Communities and people
• Growth, recovery and renewal
Accessibility
Designs should:
• Meet accessibility best practice
• Use clear typography
• Achieve strong colour contrast
• Be suitable for both digital and print formats

Deliverables
1. Principles Brochure
• A4 trifold size x 2 (online and print friendly version)
• A side to include cover side, logos side and overview of principles.
• B side full details of the principles
• Graphic to highlight the 3 c’s concept (RECOVERY Context, complexity, community centred, coordinate, communicate and capacity). Currently 3 circles.
• Can be printed and distributed electronically
2. Poster
• A1 and A3 versions
• Suitable for office and workshop display
3. Pull-Up Banner - 850 mm (W) × 2000 mm (H)
• Conference and event use
• High visual impact
• Strong branding and concise messaging
4. Social Media Tiles x 3
Updates

We are providing an extension and increasing the budget following feedback from designers. We are wanting the resources to look and feel different from the existing designs, considering either a different colour palette in the designs or different motif with the leave design. Any nature based designs should consider the Australian fauna or flora. Also suggest avoiding images in the designs. The principles are not numbered or liner in the concept of how they function. Happy to answer any further questions and thank you for your suggested concepts.

Target Market(s)

Disaster recovery practitioners, Government agencies , Non-government organisations, Community recovery workers and Community stakeholders and volunteers

Industry/Entity Type

Disaster recovery

Colors

Designer to choose colors to be used in the design.

Requirements
Must have
• Modern, warm, visually engaging, human-centred, Australian in context and different to the current design.
Nice to have
• Symbols for each principles
Should not have
• Images of disaster destruction, Emergency response imagery, Overly corporate or bureaucratic designs, Designs that focus on deficits rather than recovery and growth, avoid too much black

```html
<!DOCTYPE html>
<html lang="en">
<head>
<meta charset="utf-8">
<title>Shared Guidelines for Community Renewal – Trifold</title>
<link href="https://fonts.googleapis.com/css2?family=Lora:wght@700&family=Montserrat:wght@400;500;600;700&family=Questrial&display=swap" rel="stylesheet">
<style>
  :root{
    --backdrop:#c9c6c7;
    --charcoal:#3a3a3a;
    --charcoal-deep:#2f2f2f;
    --cream:#f8f6e6;
    --cream-edge:#eceada;
    --leaf:#6b9c2e;
    --sand:#cfc39a;
    --olive:#59613f;
    --ink:#2d2d2d;
    --ink-soft:#4a4a4a;
    --card-line:#6c6c6c;
    --rule:#cfd0bf;
  }
  *{box-sizing:border-box;margin:0;padding:0}
  html,body{width:1200px;height:2432px;overflow:hidden;background:var(--backdrop)}
  body{font-family:"Montserrat",Arial,sans-serif;color:var(--ink);position:relative}

  .spread{position:absolute;left:30px;top:813px;width:1140px;height:805px;display:flex;box-shadow:0 6px 18px rgba(0,0,0,.25)}
  .panel{position:relative;width:380px;height:805px;overflow:hidden}
  .panel--overview,.panel--partners{background:linear-gradient(180deg,var(--cream) 0%,#fbfaf0 100%)}
  .panel--partners{border-left:1px solid var(--cream-edge)}
  .panel--cover{background:var(--charcoal)}

  .section-title{font-family:"Lora",Georgia,serif;font-weight:700;font-size:20px;color:var(--ink)}
  .section-title em{font-style:normal;color:var(--leaf)}

  /* Overview panel */
  .overview-title{position:absolute;left:27px;top:36px}
  .overview-body{position:absolute;left:27px;top:70px;width:326px;font-size:8.7px;line-height:12px;color:var(--ink-soft);text-align:justify}
  .overview-body p{margin-bottom:5px}
  .overview-body h3{font-size:8.4px;font-weight:600;color:var(--leaf);margin:3px 0 4px;text-transform:uppercase}

  .successful{position:absolute;left:0;top:406px;width:380px;height:399px;background:var(--charcoal);border-top-right-radius:14px}
  .successful-tab{position:absolute;left:0;top:-22px;width:208px;height:26px;background:var(--cream);border-top-right-radius:12px;padding:5px 0 0 27px;font-weight:700;font-size:12px;color:var(--ink);letter-spacing:.2px}
  .principle-grid{position:absolute;left:27px;top:22px;width:326px;display:grid;grid-template-columns:1fr 1fr;grid-auto-rows:auto;gap:7px 12px}
  .principle-card{border:1px solid var(--card-line);border-radius:7px;padding:0 0 7px;color:#d9d9d9;font-size:8.5px;line-height:11.2px}
  .principle-card h4{font-size:8.6px;font-weight:600;color:#fff;padding:5px 7px 4px;border-bottom:1px solid var(--card-line);margin-bottom:5px;line-height:10.8px}
  .principle-card p{padding:0 7px}

  /* Partners panel */
  .partners-title{position:absolute;left:0;width:380px;top:36px;text-align:center}
  .partner-grid{position:absolute;left:35px;top:102px;width:310px;display:grid;grid-template-columns:1fr 1fr}
  .partner{height:90px;display:flex;flex-direction:column;align-items:center;justify-content:center;gap:6px;border-bottom:1px solid var(--rule);text-align:center;padding:0 8px}
  .partner:nth-child(odd){border-right:1px solid var(--rule)}
  .partner:nth-last-child(-n+2){border-bottom:none}
  .partner-mark{width:16px;height:16px;border-radius:50%;background:var(--olive)}
  .partner-name{font-size:9.5px;font-weight:600;line-height:12px;color:var(--ink)}
  .partner--single{position:absolute;left:0;width:380px;top:548px;height:56px;flex-direction:row;border:none;gap:8px}
  .development-band{position:absolute;left:0;width:380px;top:614px;height:28px;border-top:1px solid var(--rule);border-bottom:1px solid var(--rule);text-align:center;font-size:12px;letter-spacing:.6px;padding-top:6px;color:var(--ink)}
  .lead-partner{position:absolute;left:80px;top:680px;display:flex;align-items:center;gap:14px}
  .lead-mark{width:40px;height:40px;border-radius:50%;border:3px solid #2aa9d6}
  .lead-name{font-size:14px;line-height:17px;color:var(--ink-soft)}
  .lead-name span{display:block;font-size:10px;letter-spacing:1.6px;margin-top:2px}

  /* Cover panel */
  .cover-branch{position:absolute;right:0;top:0;width:300px;height:190px;background:radial-gradient(ellipse at 70% 40%,var(--leaf) 0%,rgba(107,156,46,.55) 40%,rgba(58,58,58,0) 72%)}
  .cover-title{position:absolute;left:27px;top:210px;font-family:"Questrial",Arial,sans-serif;font-weight:400;color:#fff}
  .cover-kicker{display:block;font-size:19px;letter-spacing:.4px}
  .cover-main{display:block;font-size:52px;line-height:54px;margin-top:10px}
  .cover-main span{display:block;color:var(--leaf)}
  .cover-figure{position:absolute;left:28px;top:418px;width:352px;height:387px;border-radius:48% 52% 0 0 / 30% 30% 0 0;background:linear-gradient(180deg,var(--charcoal-deep) 0%,#3e4433 28%,var(--olive) 45%,var(--sand) 72%,var(--sand) 100%)}
</style>
</head>
<body>
<main class="spread">

  <section class="panel panel--overview">
    <h2 class="section-title overview-title">Overview of <em>Principles</em></h2>
    <div class="overview-body">
      <p>Disasters can deeply impact lives and livelihoods. Working with communities recovering from disasters is complex &amp; challenging. Recovery is long-term, non-linear &amp; dynamic, particularly in the context of compounding &amp; concurrent disasters. These principles are a way to guide our efforts, our approach, our planning &amp; our decision-making.</p>
      <p>Disaster recovery is part of emergency management, which includes the broader components of prevention, preparedness &amp; response. Planning for recovery is integral to emergency preparation, and mitigation actions are often initiated as part of recovery. Disaster recovery includes built, environmental &amp; economic elements, as well as individual &amp; social wellbeing. Recovery can provide an opportunity to improve these aspects beyond previous conditions, by enhancing social &amp; natural environments, infrastructure and economies –contributing to more resilient communities.</p>
      <h3>The relationship between the principles</h3>
      <p>While all the principles are equally critical to ensure effective recovery, understanding the local &amp; broader context &amp; recognising complexity are foundational. The descriptions beneath each principle provide further guidance for working with communities in disaster recovery.</p>
    </div>

    <div class="successful">
      <div class="successful-tab">SUCCESSFUL RECOVERY</div>
      <div class="principle-grid">
        <article class="principle-card"><h4>Understand the CONTEXT</h4><p>Successful recovery is based on an understanding of the community context, with each community having its own history, values and dynamics.</p></article>
        <article class="principle-card"><h4>Recognise COMPLEXITY</h4><p>Successful recovery is responsive to the complex &amp; evolving nature of disasters &amp; their impacts on communities, including compounding, cascading and concurrent events.</p></article>
        <article class="principle-card"><h4>Use COMMUNITY-CENTRED approaches</h4><p>Successful recovery is community-centred, responsive &amp; flexible, engaging with community &amp; supporting them to move forward, with shared responsibilities.</p></article>
        <article class="principle-card"><h4>COORDINATE all activities</h4><p>Successful recovery requires a planned, coordinated &amp; adaptive approach, between community &amp; partner agencies, based on continuing assessment of impacts needs.</p></article>
        <article class="principle-card"><h4>COMMUNICATE effectively</h4><p>Successful recovery is built on effective communication between the affected community and other partners.</p></article>
        <article class="principle-card"><h4>Recognise &amp; build CAPACITY</h4><p>Successful recovery recognises, supports &amp; builds on individual, community &amp; organisational capacity and resilience.</p></article>
      </div>
    </div>
  </section>

  <section class="panel panel--partners">
    <h2 class="section-title partners-title">Our <em>Partners</em></h2>
    <div class="partner-grid">
      <div class="partner"><span class="partner-mark"></span><span class="partner-name">Federal Office of Community Services</span></div>
      <div class="partner"><span class="partner-mark"></span><span class="partner-name">Federal Office of Civic Affairs</span></div>
      <div class="partner"><span class="partner-mark"></span><span class="partner-name">Harbourline Relief Society</span></div>
      <div class="partner"><span class="partner-mark"></span><span class="partner-name">Southern Coast Regional Council</span></div>
      <div class="partner"><span class="partner-mark"></span><span class="partner-name">Westland Regional Authority</span></div>
      <div class="partner"><span class="partner-mark"></span><span class="partner-name">Island State Council</span></div>
      <div class="partner"><span class="partner-mark"></span><span class="partner-name">Northeast Regional Authority</span></div>
      <div class="partner"><span class="partner-mark"></span><span class="partner-name">Capital District Council</span></div>
      <div class="partner"><span class="partner-mark"></span><span class="partner-name">Top End Regional Council</span></div>
      <div class="partner"><span class="partner-mark"></span><span class="partner-name">Southeast State Council</span></div>
    </div>
    <div class="partner partner--single"><span class="partner-mark"></span><span class="partner-name">Eastern State Office of Readiness</span></div>
    <div class="development-band">PARTNERS IN DEVELOPMENT FROM THE</div>
    <div class="lead-partner">
      <span class="lead-mark"></span>
      <p class="lead-name">Community Wellbeing<br>Reference Network<span>AUSTRALIA</span></p>
    </div>
  </section>

  <section class="panel panel--cover">
    <div class="cover-branch" role="img" aria-label="Green leafy branch reaching in from the top right corner"></div>
    <h1 class="cover-title">
      <span class="cover-kicker">SHARED GUIDELINES FOR</span>
      <span class="cover-main">Community<span>Renewal</span></span>
    </h1>
    <div class="cover-figure" role="img" aria-label="Profile silhouette crowned with dark foliage, filled with a sand-toned scene of a city skyline, bridge and people walking together"></div>
  </section>

</main>
</body>
</html>
```